Carpentry and Home Maintenance Flyer Design

The company name is 'Mark Dellamont Building Services'.
We specialise in custom made pergolas,decks and outdoor kitchen solutions to suit ones budget and needs, we also do wide range of home maintenance and needs. These vary from security screen doors, flyscreens, timber doors, locks, garden beds, cupboards, benchtops etc.
We would like to see red used in our design, and would like it to be similar to our business card that has been designed by nexo press also.

```html
<!DOCTYPE html>
<html lang="en">
<head>
<meta charset="utf-8">
<title>Mark Dellamont Building Services – Flyers</title>
<link href="https://fonts.googleapis.com/css2?family=Roboto:wght@400;500;700&family=Roboto+Condensed:wght@400;500;700&family=Open+Sans:wght@600;700&display=swap" rel="stylesheet">
<style>
  :root{
    --red:#d0222a;
    --red-dark:#9e1218;
    --charcoal:#333335;
    --ink:#1c1c1c;
    --stage:#ececec;
  }
  *{box-sizing:border-box;margin:0;padding:0}
  html,body{width:1200px;height:842px;overflow:hidden;background:var(--stage)}
  .canvas{position:relative;width:1200px;height:842px}
  .flyer{position:absolute;width:482px;height:622px;overflow:hidden;
    box-shadow:0 6px 18px rgba(0,0,0,.25);font-family:"Roboto",Arial,sans-serif}
  .flyer--list{left:95px;top:75px}
  .flyer--gallery{left:640px;top:138px}
  .flyer__bg{position:absolute;inset:0}
  .brand{position:absolute}
  .brand__name{background:var(--red);color:#fff;font-weight:500;font-size:29px;
    height:39px;line-height:39px;padding:0 14px;text-align:center}
  .brand__tag{background:var(--charcoal);color:#fff;font-size:17px;letter-spacing:1.6px;
    font-weight:500;height:31px;line-height:31px;text-align:center}
  .flyer--list .brand{left:195px;top:14px;width:270px}
  .flyer--gallery .brand{left:0;top:21px;width:268px}
  .headline{position:absolute;left:0;right:0;text-align:center;color:var(--red);
    font-weight:700;font-size:21px}
  .flyer--list .headline{top:299px}
  .flyer--gallery .headline{top:256px}
  .services__title{position:absolute;left:39px;top:348px;color:var(--red);
    font-family:"Roboto Condensed",Arial,sans-serif;font-weight:700;font-size:19px}
  .services__list{position:absolute;top:378px;list-style:none;
    font-family:"Roboto Condensed",Arial,sans-serif;font-size:15.5px;color:var(--ink);font-weight:500}
  .services__list--a{left:39px}
  .services__list--b{left:256px}
  .services__list li{height:21.7px;display:flex;align-items:center;gap:6px}
  .tick{width:12px;height:12px;flex:none}
  .callbar{position:absolute;left:0;right:0;color:#fff;display:flex;align-items:center;
    justify-content:center;gap:8px;background:linear-gradient(180deg,#e02a31,var(--red-dark));
    font-family:"Roboto Condensed",Arial,sans-serif}
  .flyer--list .callbar{top:544px;height:45px;font-size:21px}
  .flyer--gallery .callbar{top:535px;height:50px;font-size:16.5px}
  .callbar__phone{letter-spacing:1px;font-size:1.05em}
  .phone-icon{width:15px;height:15px}
  .address{position:absolute;left:0;right:0;text-align:center;font-size:10px;
    letter-spacing:1px;color:#333}
  .flyer--list .address{top:598px}
  .flyer--gallery .address{top:593px}
  .thumbs{position:absolute;top:305px;left:20px;display:flex;gap:22px}
  .thumb{width:134px;height:98px;border-radius:10px;border:2px solid #fff;
    box-shadow:0 3px 8px rgba(0,0,0,.35)}
  .thumb--screen{background:linear-gradient(135deg,#4a2d1e,#a8643a 55%,#e3b27a)}
  .thumb--kitchen{background:linear-gradient(180deg,#3a3b3e 0 40%,#c9c7c2 40% 80%,#b98a66 80%)}
  .thumb--deck{background:radial-gradient(circle at 40% 70%,#f3b04a,#8a4a1c 45%,#1e1a17 80%)}
  .intro{position:absolute;left:36px;right:36px;top:446px;text-align:center;
    font-family:"Open Sans",Arial,sans-serif;font-weight:700;font-size:12px;line-height:1.75;color:var(--ink)}
</style>
</head>
<body>
<main class="canvas">

  <section class="flyer flyer--list">
    <svg class="flyer__bg" width="482" height="622" viewBox="0 0 482 622">
      <defs>
        <linearGradient id="paperA" x1="0" y1="0" x2="0" y2="1">
          <stop offset="0.35" stop-color="#ffffff"/><stop offset="1" stop-color="#b9babd"/>
        </linearGradient>
        <linearGradient id="pergola" x1="0" y1="0" x2="1" y2="1">
          <stop offset="0" stop-color="#e6ddd2"/><stop offset=".45" stop-color="#8c5a3c"/>
          <stop offset=".75" stop-color="#6f7a5c"/><stop offset="1" stop-color="#a79f93"/>
        </linearGradient>
        <linearGradient id="inset" x1="0" y1="0" x2="1" y2="1">
          <stop offset="0" stop-color="#3d2618"/><stop offset=".6" stop-color="#a8643a"/><stop offset="1" stop-color="#e0a56a"/>
        </linearGradient>
      </defs>
      <rect width="482" height="622" fill="url(#paperA)"/>
      <path d="M0 470 Q240 430 482 470 V540 H0Z" fill="#fff" opacity=".35"/>
      <g role="img" aria-label="Photo of a timber pergola over an outdoor seating area">
        <path d="M0 0H482V222Q330 278 170 252Q60 232 0 150Z" fill="url(#pergola)"/>
      </g>
      <path d="M0 140Q40 225 150 255Q300 290 482 228" fill="none" stroke="#333335" stroke-width="9"/>
      <path d="M0 162Q55 245 165 270Q300 295 482 246" fill="none" stroke="#9a9b9e" stroke-width="3"/>
      <path d="M0 595Q200 575 482 600" fill="none" stroke="#9a9b9e" stroke-width="6" opacity=".6"/>
      <circle cx="78" cy="198" r="52" fill="#fff"/>
      <g role="img" aria-label="Photo of a timber security screen door">
        <circle cx="78" cy="198" r="47" fill="url(#inset)"/>
      </g>
    </svg>
    <div class="brand">
      <div class="brand__name">Mark Dellamont</div>
      <div class="brand__tag">BUILDING SERVICES</div>
    </div>
    <h2 class="headline">Carpentry and Home Maintenance</h2>
    <h3 class="services__title">SERVICES</h3>
    <ul class="services__list services__list--a">
      <li><svg class="tick" viewBox="0 0 12 12"><rect x="1" y="1" width="10" height="10" rx="2" fill="none" stroke="#444" stroke-width="1.2"/><path d="M3 6l2.3 2.3L11 2" fill="none" stroke="#444" stroke-width="1.6"/></svg>Custom Made Pergolas</li>
      <li><svg class="tick" viewBox="0 0 12 12"><rect x="1" y="1" width="10" height="10" rx="2" fill="none" stroke="#444" stroke-width="1.2"/><path d="M3 6l2.3 2.3L11 2" fill="none" stroke="#444" stroke-width="1.6"/></svg>Decks</li>
      <li><svg class="tick" viewBox="0 0 12 12"><rect x="1" y="1" width="10" height="10" rx="2" fill="none" stroke="#444" stroke-width="1.2"/><path d="M3 6l2.3 2.3L11 2" fill="none" stroke="#444" stroke-width="1.6"/></svg>Outdoor Kitchen</li>
      <li><svg class="tick" viewBox="0 0 12 12"><rect x="1" y="1" width="10" height="10" rx="2" fill="none" stroke="#444" stroke-width="1.2"/><path d="M3 6l2.3 2.3L11 2" fill="none" stroke="#444" stroke-width="1.6"/></svg>Home Maintenance</li>
      <li><svg class="tick" viewBox="0 0 12 12"><rect x="1" y="1" width="10" height="10" rx="2" fill="none" stroke="#444" stroke-width="1.2"/><path d="M3 6l2.3 2.3L11 2" fill="none" stroke="#444" stroke-width="1.6"/></svg>Security Screen Doors</li>
      <li><svg class="tick" viewBox="0 0 12 12"><rect x="1" y="1" width="10" height="10" rx="2" fill="none" stroke="#444" stroke-width="1.2"/><path d="M3 6l2.3 2.3L11 2" fill="none" stroke="#444" stroke-width="1.6"/></svg>Flyscreens</li>
    </ul>
    <ul class="services__list services__list--b">
      <li><svg class="tick" viewBox="0 0 12 12"><rect x="1" y="1" width="10" height="10" rx="2" fill="none" stroke="#444" stroke-width="1.2"/><path d="M3 6l2.3 2.3L11 2" fill="none" stroke="#444" stroke-width="1.6"/></svg>Timber Doors</li>
      <li><svg class="tick" viewBox="0 0 12 12"><rect x="1" y="1" width="10" height="10" rx="2" fill="none" stroke="#444" stroke-width="1.2"/><path d="M3 6l2.3 2.3L11 2" fill="none" stroke="#444" stroke-width="1.6"/></svg>Locks</li>
      <li><svg class="tick" viewBox="0 0 12 12"><rect x="1" y="1" width="10" height="10" rx="2" fill="none" stroke="#444" stroke-width="1.2"/><path d="M3 6l2.3 2.3L11 2" fill="none" stroke="#444" stroke-width="1.6"/></svg>Garden Beds</li>
      <li><svg class="tick" viewBox="0 0 12 12"><rect x="1" y="1" width="10" height="10" rx="2" fill="none" stroke="#444" stroke-width="1.2"/><path d="M3 6l2.3 2.3L11 2" fill="none" stroke="#444" stroke-width="1.6"/></svg>Cupboards</li>
      <li><svg class="tick" viewBox="0 0 12 12"><rect x="1" y="1" width="10" height="10" rx="2" fill="none" stroke="#444" stroke-width="1.2"/><path d="M3 6l2.3 2.3L11 2" fill="none" stroke="#444" stroke-width="1.6"/></svg>Benchtops</li>
      <li><svg class="tick" viewBox="0 0 12 12"><rect x="1" y="1" width="10" height="10" rx="2" fill="none" stroke="#444" stroke-width="1.2"/><path d="M3 6l2.3 2.3L11 2" fill="none" stroke="#444" stroke-width="1.6"/></svg>And Much More...</li>
    </ul>
    <div class="callbar">
      <span>Call us now</span>
      <svg class="phone-icon" viewBox="0 0 24 24"><path fill="#fff" d="M6.6 10.8a15.1 15.1 0 0 0 6.6 6.6l2.2-2.2c.3-.3.7-.4 1-.2 1.1.4 2.3.6 3.6.6.6 0 1 .4 1 1V20c0 .6-.4 1-1 1A17 17 0 0 1 3 4c0-.6.4-1 1-1h3.5c.6 0 1 .4 1 1 0 1.3.2 2.5.6 3.6.1.3 0 .7-.2 1z"/></svg>
      <span class="callbar__phone">6140 555 018</span>
    </div>
    <p class="address">Harbourvale NSW 2599</p>
  </section>

  <section class="flyer flyer--gallery">
    <svg class="flyer__bg" width="482" height="622" viewBox="0 0 482 622">
      <defs>
        <linearGradient id="paperB" x1="0" y1="0" x2="0" y2="1">
          <stop offset="0.3" stop-color="#ffffff"/><stop offset="1" stop-color="#b9babd"/>
        </linearGradient>
        <linearGradient id="deck" x1="0" y1="0" x2="0" y2="1">
          <stop offset="0" stop-color="#e8e3da"/><stop offset=".25" stop-color="#7a5a44"/>
          <stop offset=".5" stop-color="#b4643a"/><stop offset="1" stop-color="#8a3f22"/>
        </linearGradient>
      </defs>
      <rect width="482" height="622" fill="url(#paperB)"/>
      <g role="img" aria-label="Photo of a timber deck with a raised garden planter">
        <path d="M0 0H482V190Q430 218 340 226Q230 232 150 236Q60 240 0 225Z" fill="url(#deck)"/>
      </g>
      <path d="M40 0Q5 40 30 90" fill="none" stroke="#333335" stroke-width="10"/>
      <path d="M0 225Q120 260 260 245Q380 232 482 190" fill="none" stroke="#fff" stroke-width="8"/>
      <path d="M0 240Q150 275 300 255Q400 240 482 205" fill="none" stroke="#a7a8ab" stroke-width="3"/>
      <path d="M0 600Q200 575 482 598" fill="none" stroke="#9a9b9e" stroke-width="6" opacity=".6"/>
      <circle cx="152" cy="187" r="46" fill="var(--red)" stroke="#fff" stroke-width="2" stroke-dasharray="3 2"/>
      <circle cx="152" cy="187" r="38" fill="#5d5e61" stroke="#fff" stroke-width="2"/>
      <text x="152" y="175" text-anchor="middle" fill="#fff" font-family="Open Sans, Arial, sans-serif" font-weight="700" font-size="10">NO JOB IS</text>
      <text x="152" y="190" text-anchor="middle" fill="#fff" font-family="Open Sans, Arial, sans-serif" font-weight="700" font-size="10">TOO BIG OR</text>
      <text x="152" y="205" text-anchor="middle" fill="#fff" font-family="Open Sans, Arial, sans-serif" font-weight="700" font-size="10">TOO SMALL</text>
    </svg>
    <div class="brand">
      <div class="brand__name">Mark Dellamont</div>
      <div class="brand__tag">BUILDING SERVICES</div>
    </div>
    <h2 class="headline">Carpentry and Home Maintenance</h2>
    <div class="thumbs">
      <div class="thumb thumb--screen" role="img" aria-label="Photo of a timber security screen door"></div>
      <div class="thumb thumb--kitchen" role="img" aria-label="Photo of a stainless outdoor kitchen"></div>
      <div class="thumb thumb--deck" role="img" aria-label="Photo of a lit timber deck at night"></div>
    </div>
    <p class="intro">We specialise in custom made pergolas,decks and outdoor kitchen solutions to suit ones budget and needs, we also do wide range of home maintenance and needs.</p>
    <div class="callbar">
      <span>Call now for FREE no obligation quote</span>
      <svg class="phone-icon" viewBox="0 0 24 24"><path fill="#fff" d="M6.6 10.8a15.1 15.1 0 0 0 6.6 6.6l2.2-2.2c.3-.3.7-.4 1-.2 1.1.4 2.3.6 3.6.6.6 0 1 .4 1 1V20c0 .6-.4 1-1 1A17 17 0 0 1 3 4c0-.6.4-1 1-1h3.5c.6 0 1 .4 1 1 0 1.3.2 2.5.6 3.6.1.3 0 .7-.2 1z"/></svg>
      <span class="callbar__phone">6140 555 018</span>
    </div>
    <p class="address">Harbourvale NSW 2599</p>
  </section>

</main>
</body>
</html>
```